Aviation security consulting company needs a website

We need a website design for Brisk Holloway, and aviation security consulting company. Brisk Holloway (www.briskholloway.example) is an aviation security consulting company that works with government and industry stakeholders in over 60 countries on aviation security strategy, governance, and oversight at the regulatory and operational level.
Brisk Holloway is strongly internationally focused.
The website required should be simple, corporate, serious, and communicate professionalism, reliability and honesty. We are trying to give the company a feeling of being well established.
The attached files include the company logo, along with examples of company web page styles that we like.
The Brisk Holloway website need only be around five pages long (landing page, who we are, our services, our clients, contact), though don't feel limited to only five pages.
The existing website (www.briskholloway.example) was rushed and put together using Wix. We don't love the existing website as it looks too amateur, so don't use it as a template.
There is no requirement for any online sales tools to be included in the site. The site is purely informational, with the option of people making contact via email.

```html
<!DOCTYPE html>
<html lang="en">
<head>
<meta charset="utf-8">
<title>Brisk Holloway — Aviation Security Consulting</title>
<link rel="stylesheet" href="https://fonts.googleapis.com/css2?family=Questrial&family=Open+Sans:wght@400;600;700&family=Oswald:wght@500&display=swap">
<style>
:root{
  --navy:#0f1b48;
  --navy-deep:#0a1336;
  --royal:#243b7d;
  --ink:#1c2c66;
  --text:#555a66;
  --muted:#8a8f99;
  --white:#ffffff;
  --dark:#262626;
  --darker:#1b1b1b;
  --footer-text:#c9c9c9;
}
*{box-sizing:border-box;margin:0;padding:0}
html,body{width:1200px;height:2190px;overflow:hidden;background:var(--white)}
body{font-family:"Open Sans",Arial,sans-serif;color:var(--text);position:relative}
.display{font-family:"Questrial","Open Sans",sans-serif}
section,header,footer{position:absolute;left:0;width:1200px}

/* header */
.site-header{top:0;height:90px;background:var(--navy);border-top:4px solid var(--navy-deep)}
.brand{position:absolute;left:102px;top:20px;display:flex;align-items:center;gap:10px;color:var(--white)}
.brand-mark{width:48px;height:48px;border:4px solid var(--white)}
.brand-name{font-family:"Questrial",sans-serif;font-size:28px;line-height:1}
.brand-tag{font-size:11px;letter-spacing:1px;margin-top:3px}
.main-nav{position:absolute;left:478px;top:0;display:flex;height:86px;align-items:center}
.main-nav a{color:var(--white);text-decoration:none;font-size:13px;font-weight:600;margin-right:52px}
.main-nav .is-active{background:var(--navy-deep);height:86px;width:88px;display:flex;align-items:center;justify-content:center;margin-right:30px}
.main-nav .is-active span{border:4px solid var(--white);width:72px;height:72px;display:flex;align-items:center;justify-content:center}
.search-btn{position:absolute;left:1068px;top:26px;width:34px;height:34px;border-radius:50%;background:var(--white);display:flex;align-items:center;justify-content:center}

/* hero */
.hero{top:90px;height:498px;background:radial-gradient(ellipse at 35% 40%,#cfcfcf 0%,#6e6e6e 30%,#2a2a2a 60%,#0d0d0d 100%)}
.hero-caption{position:absolute;left:620px;top:168px;width:482px;height:158px;background:rgba(0,0,0,.72);padding:20px 36px;color:var(--white)}
.hero-caption h1{font-family:"Questrial",sans-serif;font-weight:400;font-size:33px;margin-bottom:18px}
.hero-caption p{font-size:13px;line-height:24px;padding-left:20px}
.hero-arrow{position:absolute;top:232px;width:30px;height:30px;border-radius:50%;background:rgba(255,255,255,.7)}

/* welcome */
.welcome{top:588px;height:294px;background:var(--royal);text-align:center;color:var(--white)}
.section-title{font-family:"Questrial",sans-serif;font-weight:400;font-size:28px;display:flex;align-items:center;justify-content:center;gap:10px}
.title-mark{width:28px;height:28px;border:3px solid currentColor}
.welcome .section-title{margin-top:40px}
.welcome p{width:1036px;margin:18px auto 0;font-size:11px;line-height:26px}
.btn{display:inline-block;font-size:12px;font-weight:600;padding:0 18px;height:46px;line-height:46px;color:var(--white);text-decoration:none}
.btn-dark{background:var(--navy-deep);margin-right:8px}
.btn-outline{border:2px solid var(--white);line-height:42px}
.welcome .actions{margin-top:26px}

/* services */
.services{top:882px;height:416px;background:var(--white)}
.services .section-title{color:#333;margin-top:36px}
.pager{position:absolute;right:64px;top:44px;color:#bbb;font-size:13px}
.service{position:absolute;width:300px;padding-left:66px}
.service-icon{position:absolute;left:0;top:0;width:52px;height:52px;border:4px solid var(--ink);display:flex;align-items:center;justify-content:center}
.service h3{font-family:"Questrial",sans-serif;font-weight:400;font-size:15px;color:var(--ink);margin-bottom:16px}
.service p{font-size:11px;line-height:21px;color:var(--muted)}
.service a{display:inline-block;font-size:11px;color:var(--ink);margin-top:10px}

/* sectors */
.sectors{top:1298px;height:486px;background:radial-gradient(ellipse at 50% 40%,#3a3029 0%,#1a1714 55%,#0c0c0c 100%);color:var(--white);text-align:center}
.sectors .section-title{margin-top:54px}
.sector{position:absolute;top:120px;width:234px}
.sector-photo{width:234px;height:170px;border:4px solid var(--white)}
.sector h3{font-family:"Questrial",sans-serif;font-weight:400;font-size:15px;margin-top:16px}
.sector p{font-size:11px;line-height:21px;margin-top:6px}
.sector .btn{height:36px;line-height:32px;border:2px solid var(--white);background:var(--navy);margin-top:14px;padding:0 20px}
.side-arrow{position:absolute;top:190px;color:#999;font-size:18px}

/* clients */
.clients{top:1784px;height:128px;background:linear-gradient(#fff,#ececec);display:flex;align-items:center;justify-content:space-around;padding:0 110px}
.client{font-family:"Oswald",sans-serif;font-size:30px;color:#a3a3a3}

/* footer */
.site-footer{top:1912px;height:214px;background:var(--dark);color:var(--footer-text)}
.col{position:absolute;top:28px}
.col h4{font-family:"Questrial",sans-serif;font-weight:400;font-size:16px;color:var(--white);margin-bottom:16px}
.col p,.col li{font-size:11px;line-height:20px}
.contact-line{display:flex;align-items:center;gap:14px;margin-top:10px}
.phone{font-size:16px}
.tweet{display:flex;gap:10px;margin-bottom:10px}
.tw-icon{width:16px;height:16px;background:var(--white);border-radius:2px;flex:none;margin-top:2px}
.signup{display:flex;margin-top:16px}
.signup span{width:184px;height:38px;background:#333;font-size:10px;line-height:38px;padding-left:12px;color:#999}
.signup b{width:80px;height:38px;background:var(--royal);color:var(--white);font-size:13px;line-height:38px;text-align:center}
.social{list-style:none}
.social li{display:flex;align-items:center;gap:12px;margin-bottom:8px}
.dot{width:8px;height:8px;border-radius:50%;background:var(--white)}
.legal{position:absolute;left:0;top:2126px;width:1200px;height:64px;background:var(--darker);color:var(--white);font-size:11px;text-align:center;line-height:64px}
</style>
</head>
<body>

<header class="site-header">
  <div class="brand">
    <div class="brand-mark"></div>
    <div>
      <div class="brand-name">Brisk Holloway</div>
      <div class="brand-tag">aviation security consulting</div>
    </div>
  </div>
  <nav class="main-nav">
    <a class="is-active" href="#"><span>Home</span></a>
    <a href="#">Who we are</a>
    <a href="#">Our Services</a>
    <a href="#">Our Clients</a>
    <a href="#">Contact</a>
  </nav>
  <div class="search-btn"><svg width="12" height="12" viewBox="0 0 12 12"><circle cx="5" cy="5" r="3.5" fill="none" stroke="#0f1b48" stroke-width="2"/><line x1="7.5" y1="7.5" x2="11" y2="11" stroke="#0f1b48" stroke-width="2"/></svg></div>
</header>

<section class="hero" role="img" aria-label="Black and white photo of a passenger jet parked on a night apron">
  <div class="hero-arrow" style="left:42px"></div>
  <div class="hero-arrow" style="left:1128px"></div>
  <div class="hero-caption">
    <h1>Aviation Security Consulting</h1>
    <p>Neque porro quisquam est, qui dolorem ipsum quia dolor sit amet, consectetur, adipisci velit, sed quia non numq...</p>
  </div>
</section>

<section class="welcome">
  <h2 class="section-title"><span class="title-mark"></span>Welcome to Brisk Holloway</h2>
  <p>Nemo enim ipsam voluptatem quia voluptas sit aspernatur aut odit aut fugit, sed quia consequuntur magni dolores eos qui ratione voluptatem sequi nesciunt. Neque porro quisquam est, qui dolorem ipsum quia dolor sit amet, consectetur, adipisci velit, sed quia non numquam eius modi tempora incidunt ut labore et dolore magnam aliquam quaerat enim ad minima veniam, quis nostrum exercitationem ullam corporis suscipit laboriosam, nisi ut aliquid ex ea commodi consequatur...</p>
  <div class="actions"><a class="btn btn-dark" href="#">Read More Info</a><a class="btn btn-outline" href="#">Get Start Today</a></div>
</section>

<section class="services">
  <h2 class="section-title"><span class="title-mark" style="color:var(--ink)"></span>Services Provided</h2>
  <div class="pager">‹ ›</div>

  <article class="service" style="left:98px;top:108px">
    <div class="service-icon"><svg width="26" height="22" viewBox="0 0 26 22"><path d="M3 2h20v13H10l-5 5v-5H3z" fill="#1c2c66"/></svg></div>
    <h3>Business Continuity</h3>
    <p>Phasellus facilisis, nunc in undo tump lacinia auctor, quisquam eros lacus...</p>
    <a>Read More →</a>
  </article>
  <article class="service" style="left:452px;top:108px">
    <div class="service-icon"><svg width="24" height="24" viewBox="0 0 24 24"><circle cx="12" cy="12" r="11" fill="none" stroke="#1c2c66" stroke-width="2"/><rect x="7" y="11" width="10" height="7" fill="#1c2c66"/><path d="M9 11V8a3 3 0 0 1 6 0v3" fill="none" stroke="#1c2c66" stroke-width="2"/></svg></div>
    <h3>Cyber Security</h3>
    <p>Phasellus facilisis, nunc in undo tump lacinia auctor, quisquam eros lacus...</p>
    <a>Read More →</a>
  </article>
  <article class="service" style="left:805px;top:108px">
    <div class="service-icon"><svg width="20" height="26" viewBox="0 0 20 26"><circle cx="10" cy="9" r="7" fill="none" stroke="#1c2c66" stroke-width="2"/><rect x="6" y="18" width="8" height="5" fill="#1c2c66"/></svg></div>
    <h3>Master Planing</h3>
    <p>Phasellus facilisis, nunc in undo tump lacinia auctor, quisquam eros lacus...</p>
    <a>Read More →</a>
  </article>
  <article class="service" style="left:98px;top:262px">
    <div class="service-icon"><svg width="26" height="24" viewBox="0 0 26 24"><line x1="3" y1="2" x2="3" y2="23" stroke="#1c2c66" stroke-width="2"/><path d="M4 3h19v11H4z" fill="none" stroke="#1c2c66" stroke-width="2"/><path d="M4 3h6v5h6v6h-6V8H4z" fill="#1c2c66"/></svg></div>
    <h3>Organisation &amp; Covernance</h3>
    <p>Phasellus facilisis, nunc in undo tump lacinia auctor, quisquam eros lacus...</p>
    <a>Read More →</a>
  </article>
  <article class="service" style="left:452px;top:262px">
    <div class="service-icon"><svg width="24" height="24" viewBox="0 0 24 24"><path d="M11 3a10 10 0 1 0 10 10H11z" fill="#1c2c66"/><path d="M13 1v10h10A10 10 0 0 0 13 1z" fill="#1c2c66"/></svg></div>
    <h3>Strategic Planing</h3>
    <p>Phasellus facilisis, nunc in undo tump lacinia auctor, quisquam eros lacus...</p>
    <a>Read More →</a>
  </article>
  <article class="service" style="left:805px;top:262px">
    <div class="service-icon"><svg width="26" height="24" viewBox="0 0 26 24"><rect x="2" y="2" width="22" height="15" fill="none" stroke="#1c2c66" stroke-width="3"/><rect x="10" y="17" width="6" height="4" fill="#1c2c66"/><rect x="6" y="21" width="14" height="2" fill="#1c2c66"/></svg></div>
    <h3>Technology Evaluation</h3>
    <p>Phasellus facilisis, nunc in undo tump lacinia auctor, quisquam eros lacus...</p>
    <a>Read More →</a>
  </article>
</section>

<section class="sectors">
  <h2 class="section-title"><span class="title-mark"></span>Sectors We Serve</h2>
  <span class="side-arrow" style="left:58px">◀</span>
  <span class="side-arrow" style="left:1126px">▶</span>

  <article class="sector" style="left:98px">
    <div class="sector-photo" role="img" aria-label="Photo of engineers beside a jet engine" style="background:linear-gradient(#b9c9dc,#6b7c8e 60%,#3c4650)"></div>
    <h3>Critical Infrastructure</h3>
    <p>Numquam eius modi tempora incidunt<br>labore et dolore magnam...</p>
    <a class="btn" href="#">Read More</a>
  </article>
  <article class="sector" style="left:355px">
    <div class="sector-photo" role="img" aria-label="Photo of ground crew loading an aircraft" style="background:linear-gradient(#8fa6c4,#2e3f5e 60%,#1a2234)"></div>
    <h3>High Treatment Environment</h3>
    <p>Numquam eius modi tempora incidunt<br>labore et dolore magnam...</p>
    <a class="btn" href="#">Read More</a>
  </article>
  <article class="sector" style="left:611px">
    <div class="sector-photo" role="img" aria-label="Photo of a refinery lit up at dusk" style="background:linear-gradient(#5d6fa3,#7a5a88 50%,#2b2630)"></div>
    <h3>Oil &amp; Gas</h3>
    <p>Numquam eius modi tempora incidunt<br>labore et dolore magnam...</p>
    <a class="btn" href="#">Read More</a>
  </article>
  <article class="sector" style="left:867px">
    <div class="sector-photo" role="img" aria-label="Photo of a plane flying over a city at sunset" style="background:linear-gradient(#f0a040,#d56a2c 55%,#3a2a2a)"></div>
    <h3>Transport</h3>
    <p>Numquam eius modi tempora incidunt<br>labore et dolore magnam...</p>
    <a class="btn" href="#">Read More</a>
  </article>
</section>

<section class="clients">
  <span class="client">SWIFTA</span>
  <span class="client">Morvale</span>
  <span class="client">CONSULAR</span>
  <span class="client">Tarnesse</span>
  <span class="client">verdo</span>
  <span class="client">HALMOR</span>
</section>

<footer class="site-footer">
  <div class="col" style="left:98px">
    <h4>Contact us</h4>
    <p>482 Harrow Field Ave.<br>Lakemont, OR 97000 USA</p>
    <div class="contact-line"><svg width="16" height="16" viewBox="0 0 16 16"><path d="M3 1l3 3-2 2c1 2 3 4 5 5l2-2 3 3-2 3C6 14 2 10 1 3z" fill="none" stroke="#c9c9c9" stroke-width="1.3"/></svg><span class="phone">(555) 014-2286</span></div>
    <div class="contact-line"><svg width="16" height="12" viewBox="0 0 16 12"><rect x="1" y="1" width="14" height="10" fill="none" stroke="#c9c9c9" stroke-width="1.3"/><path d="M1 1l7 6 7-6" fill="none" stroke="#c9c9c9" stroke-width="1.3"/></svg><span style="font-size:13px">info@briskholloway.example</span></div>
  </div>
  <div class="col" style="left:368px;width:230px">
    <h4>Latest Tweet`s</h4>
    <div class="tweet"><span class="tw-icon"></span><p>Good morning .... wherever you are today! All of us at ...See more here http://lnk.example/q7Rd2</p></div>
    <div class="tweet"><span class="tw-icon"></span><p>Good morning .... wherever you are today! All of us at ...See more here http://lnk.example/q7Rd2</p></div>
  </div>
  <div class="col" style="left:665px;top:36px;width:270px">
    <h4>Newsletter</h4>
    <p>Excepteur sint occaecat cupidatat non proident, sunt in culpa qui officia deserunt mollit anim</p>
    <div class="signup"><span>Enter your email address</span><b>Sign Up</b></div>
  </div>
  <div class="col" style="left:1003px">
    <h4>Social Media</h4>
    <ul class="social">
      <li><span class="dot"></span>Friendwall</li>
      <li><span class="dot"></span>Chirpline</li>
      <li><span class="dot"></span>Circlenet</li>
      <li><span class="dot"></span>Viewcast</li>
    </ul>
  </div>
</footer>
<div class="legal">© 2016 BRISKHOLLOWAY - ALL RIGHTS RESERVED</div>

</body>
</html>
```